Investment Advisor E-Newsletter Banner Design

I need a banner designed for an email newsletter that will be sent monthly to clients and prospects. We want to see designs that are elegant and use our logo well. The banner should be 922x150px and should go well with the www.bhtlwest.com website. Should include Logo and email and phone number.

Target Market(s)

High net worth investors

Number of Pages Required

1 page

Requirements
Must have
• logo, place for email (info@bhtlwest.com) and phone number (555-219-0387), colors and design that work well with www.bhtlwest.com website

```html
<!DOCTYPE html>
<html lang="en">
<head>
<meta charset="utf-8">
<title>Keystone Harbor – Newsletter Banner</title>
<link href="https://fonts.googleapis.com/css2?family=Didact+Gothic&family=Cormorant+Upright:wght@500&display=swap" rel="stylesheet">
<style>
  :root {
    --night-deep: #1d1d4a;
    --night-violet: #4a3f86;
    --night-blue: #3d5aa8;
    --icon-blue: #2f6fd0;
    --mark-blue: #3a78d8;
    --text-light: #f4f4fb;
  }
  html, body {
    margin: 0;
    padding: 0;
    width: 1200px;
    height: 195px;
    overflow: hidden;
    background: var(--night-deep);
  }
  .banner {
    position: relative;
    width: 1200px;
    height: 195px;
    overflow: hidden;
    font-family: "Didact Gothic", sans-serif;
    color: var(--text-light);
  }
  .banner__skyline {
    position: absolute;
    inset: 0;
    background:
      radial-gradient(ellipse 260px 120px at 1010px 170px, rgba(170, 110, 180, 0.5), transparent 70%),
      radial-gradient(ellipse 300px 160px at 600px 40px, rgba(120, 110, 190, 0.4), transparent 70%),
      linear-gradient(90deg, var(--night-deep) 0%, #2c2b62 22%, var(--night-violet) 48%, #3b3f86 72%, var(--night-blue) 100%);
  }
  .contact {
    position: absolute;
    left: 110px;
    top: 48px;
    margin: 0;
    padding: 0;
    list-style: none;
  }
  .contact__item {
    display: flex;
    align-items: center;
    height: 40px;
    margin-bottom: 22px;
    font-size: 22px;
    letter-spacing: 1.2px;
  }
  .contact__icon {
    width: 40px;
    height: 40px;
    flex: none;
    margin-right: 23px;
  }
  .brand-mark {
    position: absolute;
    left: 545px;
    top: 50px;
    width: 96px;
    height: 96px;
    background: var(--mark-blue);
    opacity: 0.85;
  }
  .brand {
    position: absolute;
    left: 765px;
    top: 50px;
    margin: 0;
    font-family: "Cormorant Upright", serif;
    font-weight: 500;
    color: var(--text-light);
  }
  .brand__name {
    display: block;
    font-size: 40px;
    line-height: 46px;
    white-space: nowrap;
  }
  .brand__tagline {
    display: block;
    margin-top: 10px;
    font-size: 16px;
    line-height: 18px;
    white-space: nowrap;
  }
</style>
</head>
<body>
  <header class="banner">
    <div class="banner__skyline" role="img" aria-label="Night city skyline with lit towers in violet and blue tones"></div>

    <ul class="contact">
      <li class="contact__item">
        <svg class="contact__icon" viewBox="0 0 34 34" aria-hidden="true">
          <circle cx="17" cy="17" r="17" fill="var(--icon-blue)"/>
          <path d="M12.2 9.5c.6-.4 1.3-.3 1.7.3l1.6 2.5c.4.6.3 1.3-.2 1.7l-1.1.9c.7 1.8 2.2 3.5 4 4.5l1-1c.5-.5 1.2-.5 1.700-.1l2.4 1.8c.6.4.7 1.2.3 1.7l-1 1.4c-.6.8-1.7 1.1-2.7.7-4.4-1.7-7.6-5.1-9-9.5-.3-1 .1-2.1.9-2.7z" fill="#ffffff"/>
        </svg>
        <span>555-219-0387</span>
      </li>
      <li class="contact__item">
        <svg class="contact__icon" viewBox="0 0 34 34" aria-hidden="true">
          <circle cx="17" cy="17" r="17" fill="var(--icon-blue)"/>
          <rect x="9" y="11.5" width="16" height="11" rx="1" fill="#ffffff"/>
          <path d="M9.5 12.2 17 18l7.5-5.8" fill="none" stroke="var(--icon-blue)" stroke-width="1.4"/>
        </svg>
        <span>info@bhtlwest.com</span>
      </li>
    </ul>

    <div class="brand-mark" aria-hidden="true"></div>

    <p class="brand">
      <span class="brand__name">Keystone Harbor</span>
      <span class="brand__tagline">Advisory &amp; Planning, Inc.</span>
    </p>
  </header>
</body>
</html>
```